Business card for a "family office" company

Please provide professional looking business card designs, incorporating the attached logo and below details. Harrowmere Holdings Pty Ltd is a family office / financial investment company. We are looking for a modern, professional and contemporary card design.

Industry/Entity Type

Finance

Contact Information for Business Card

Name: Dean Malcott
Title: Director
Company: Harrowmere Holdings Pty Ltd
Email: harrowlead@ozmailnet.com.au
Mobile: 0492 635 718
Address: 3/412 Bramwood Parade, Pellingford WA 6019, Australia

Requirements
Must have
• All details above and the logo. logo only on back side. incorporate colours of logo
Nice to have
• up to you
Should not have
• ?

```html
<!DOCTYPE html>
<html lang="en">
<head>
<meta charset="utf-8">
<title>Harrowmere Holdings – Business Card</title>
<link href="https://fonts.googleapis.com/css2?family=Source+Sans+3:wght@300;400;600&display=swap" rel="stylesheet">
<style>
  :root {
    --navy: #1d1d5c;
    --navy-deep: #15154a;
    --white: #ffffff;
    --fold: #d9dbe2;
    --backdrop: #ecebe8;
    --rule: rgba(255,255,255,0.55);
  }
  * { box-sizing: border-box; margin: 0; padding: 0; }
  html, body { width: 1200px; height: 1200px; overflow: hidden; }
  body {
    background: var(--backdrop);
    font-family: "Source Sans 3", sans-serif;
    display: flex; flex-direction: column; align-items: center; justify-content: center;
    gap: 60px;
  }
  .card {
    position: relative; width: 900px; height: 514px;
    background: var(--white); overflow: hidden;
    box-shadow: 0 6px 18px rgba(0,0,0,0.12);
  }
  .brand {
    display: flex; align-items: center; gap: 14px;
    font-weight: 400; letter-spacing: 0.14em; text-transform: uppercase;
    font-size: 28px; white-space: nowrap;
  }
  .brand-mark { width: 18px; height: 18px; background: currentColor; }
  .ribbon {
    position: absolute; background: var(--navy); color: var(--white);
    display: flex; align-items: center; padding-left: 34px;
    font-weight: 600; font-size: 22px; white-space: nowrap;
  }
  .ribbon-fold { position: absolute; width: 0; height: 0; }

  /* logo side */
  .logo-side .logo-block {
    position: absolute; left: 200px; top: 70px; width: 470px; height: 250px;
    background: var(--navy); color: var(--white);
    display: flex; align-items: center; justify-content: center;
  }
  .logo-side .ribbon { left: 430px; top: 290px; width: 470px; height: 130px; }
  .logo-side .fold-top {
    left: 412px; top: 290px;
    border-right: 18px solid var(--fold); border-top: 18px solid transparent;
  }
  .logo-side .fold-bottom {
    left: 412px; top: 402px;
    border-right: 18px solid var(--fold); border-bottom: 18px solid transparent;
  }

  /* details side */
  .details-side .head { position: absolute; inset: 0 0 auto 0; height: 250px; }
  .details-side .brand { position: absolute; left: 330px; top: 76px; color: var(--navy); }
  .details-side .ribbon { left: 620px; top: 150px; width: 280px; height: 70px; font-size: 19px; padding-left: 26px; }
  .details-side .fold-bottom {
    left: 620px; top: 220px;
    border-top: 16px solid var(--navy-deep); border-left: 16px solid transparent;
  }
  .details-side .contact {
    position: absolute; left: 0; right: 0; top: 250px; bottom: 0;
    background: var(--navy); color: var(--white);
    padding: 18px 70px 0 60px;
    list-style: none;
  }
  .contact-row {
    display: flex; align-items: center; gap: 22px;
    min-height: 58px; border-bottom: 1px solid var(--rule);
    font-size: 19px; font-weight: 400;
  }
  .contact-row:last-child { border-bottom: none; padding-top: 8px; line-height: 1.3; }
  .contact-row svg { width: 26px; height: 26px; flex: none; fill: var(--white); }
  .person-name { font-size: 30px; font-weight: 300; }
  .person-title { font-size: 18px; font-weight: 300; padding-left: 12px; border-left: 2px solid var(--white); }
</style>
</head>
<body>

  <section class="card logo-side" aria-label="Card back with company name">
    <div class="logo-block">
      <div class="brand"><span class="brand-mark"></span>Harrowmere Holdings</div>
    </div>
    <div class="ribbon-fold fold-top"></div>
    <div class="ribbon-fold fold-bottom"></div>
    <div class="ribbon">Harrowmere Holdings Pty Ltd</div>
  </section>

  <section class="card details-side" aria-label="Card front with contact details">
    <div class="head">
      <div class="brand"><span class="brand-mark"></span>Harrowmere Holdings</div>
      <div class="ribbon">Harrowmere Holdings Pty Ltd</div>
      <div class="ribbon-fold fold-bottom"></div>
    </div>
    <ul class="contact">
      <li class="contact-row">
        <svg viewBox="0 0 24 24" aria-hidden="true"><circle cx="12" cy="7" r="5"/><path d="M2 23c0-6 4.5-9 10-9s10 3 10 9z"/></svg>
        <span class="person-name">Dean Malcott</span><span class="person-title">Director</span>
      </li>
      <li class="contact-row">
        <svg viewBox="0 0 24 24" aria-hidden="true"><path d="M7 1h10a2 2 0 0 1 2 2v18a2 2 0 0 1-2 2H7a2 2 0 0 1-2-2V3a2 2 0 0 1 2-2zm1 3v8h8V4zm0 10v2h2v-2zm3 0v2h2v-2zm3 0v2h2v-2zm-6 3v2h2v-2zm3 0v2h2v-2zm3 0v2h2v-2z"/></svg>
        <span>0492 635 718</span>
      </li>
      <li class="contact-row">
        <svg viewBox="0 0 24 24" aria-hidden="true"><path d="M1 4h22v16H1zm2 2v.4l9 6.6 9-6.6V6zm0 2.9V18h18V8.9l-9 6.6z"/></svg>
        <span>harrowlead@ozmailnet.com.au</span>
      </li>
      <li class="contact-row">
        <svg viewBox="0 0 24 24" aria-hidden="true"><path d="M12 1a8 8 0 0 0-8 8c0 6 8 14 8 14s8-8 8-14a8 8 0 0 0-8-8zm0 11a3 3 0 1 1 0-6 3 3 0 0 1 0 6z"/></svg>
        <span>3/412 Bramwood Parade<br>Pellingford WA 6019, Australia</span>
      </li>
    </ul>
  </section>

</body>
</html>
```